Plumbing Contractor Website Design

We are working with a Plumbing contractor in CA called KP Ductworks.

Some sites to use for content/competitors and inspiration:

https://www.pipelarkservice.example
https://www.drainowlpros.example
https://gantrybay.example/web/contractor/ (lots of contractor website designs we've approved and continue to show clients)

Thank you for taking the time to consider designing a website for us. We are web developers based in Stockton, CA, USA. Most of our projects go through the same process. Understanding this process may help you win a project with us. We custom-code all of our websites in-house. We don’t have any requirements as to what tools you use for your design, but we prefer Figma files. For any design that we label as four-stars, we send it to the client for review. The client picks the final design they want us to use. Once we complete this process, we will continue to show additional clients all the four-star sites and purchase them later. Your designs will have multiple chances to sell. For better chances of success, we ask that you follow these guidelines.

IMAGES:
If you use any images or icons in the design, we ask that you have a link to the asset so we can purchase the image/icon. Most of the designs we submit do not have the customer’s images on them unless they have some great images. Be creative; show us the feeling you are trying to portray with your image choices. Use any royalty-free site you choose. We subscribe to Velmora and mainly use their images, but we can purchase images outside of Velmora.

PLEASE NOTE: we will not submit designs to clients with watermarks on the images.

FONTS:
We ask that you identify the fonts used in the design. This can be done in a message if you want. We typically use Zintari Fonts and Velmora Fonts.

CONTENT:
We're always open to different content and ideas. We often submit designs with stock images so the client can see our vision. We typically take pictures after the website launch to use their images with our vision. Lorem Ipsum is fine for paragraphs, but we ask that you write the headers in correct English. We want to be able to show the vision and identify the sections of the website.

INSPIRATION:
We typically add a couple of links in the brief of websites we like to help you get started in your design.

REVISIONS:
We do not often ask for revisions of the designs unless we see something in the design that may not appeal to the client. If there are slight changes that we want to make, we do that in the development process.

FEEDBACK:
We rarely give feedback on designs during the design process. We are working on many website projects and do not have the time to provide feedback. We usually respond if your request is well thought out and asks specific questions, but a note asking “feedback, please” usually goes unanswered

```html
<!DOCTYPE html>
<html lang="en">
<head>
<meta charset="utf-8">
<title>KP Ductworks – Plumbing Contractor</title>
<link href="https://fonts.googleapis.com/css2?family=Poppins:ital,wght@0,300;0,400;0,500;0,600;0,700;1,400&display=swap" rel="stylesheet">
<style>
:root{
  --blue:#0a5b8c;
  --blue-dark:#074a73;
  --ink:#1d1d1d;
  --muted:#6f6f6f;
  --line:#e3e3e3;
  --dark:#2b2b2b;
  --dark-box:#323232;
  --white:#ffffff;
}
*{box-sizing:border-box;margin:0;padding:0}
html,body{width:1200px;height:3916px;overflow:hidden}
body{font-family:"Poppins",sans-serif;color:var(--ink);background:var(--white);position:relative}
.abs{position:absolute}
b,strong{font-weight:700}

/* header */
.header{left:0;top:0;width:1200px;height:80px;background:var(--white);border-bottom:1px solid var(--line)}
.logo{left:88px;top:8px;display:flex;align-items:center;gap:8px}
.logo-mark{width:40px;height:40px;border-radius:50%;background:var(--blue)}
.logo-name{font-size:13px;font-weight:700;color:var(--blue);line-height:1.1;width:70px}
.topbar{left:388px;top:0;width:524px;height:36px;background:var(--blue);clip-path:polygon(0 0,100% 0,96% 100%,5% 100%)}
.topbar-item{top:10px;color:var(--white);font-size:13px;display:flex;align-items:center;gap:6px}
.flag{width:20px;height:13px;background:#c9d3e6;border:1px solid #fff}
.nav{top:52px;left:0;width:1200px;font-size:12.5px;color:#555}
.nav span{position:absolute}
.emergency{left:890px;top:0;width:310px;height:80px;background:var(--blue);clip-path:polygon(6% 0,100% 0,100% 100%,0 100%)}
.emergency .ring{position:absolute;left:44px;top:20px;width:36px;height:36px;border:2px solid var(--white);border-radius:50%;color:#fff;font-size:10px;font-weight:600;display:flex;align-items:center;justify-content:center}
.emergency .lbl{position:absolute;left:86px;top:20px;color:#fff;font-size:12.5px}
.emergency .num{position:absolute;left:86px;top:38px;color:#fff;font-size:15px}

/* hero */
.hero{left:0;top:80px;width:1200px;height:551px;background:linear-gradient(100deg,#3a3d42 0%,#5a5d62 45%,#8a8780 70%,#b9b4aa 100%)}
.hero-title{left:88px;top:196px;font-size:47px;font-weight:300;color:#fff;line-height:53px}
.hero-title b{font-weight:700}
.hero-text{left:88px;top:362px;width:420px;color:#fff;font-size:12.5px;line-height:22px}
.btn-white{background:#fff;color:var(--ink);font-size:13px;font-weight:600;display:flex;align-items:center;justify-content:center}
.hero-btn{left:88px;top:426px;width:136px;height:43px}

/* schedule */
.schedule{left:271px;top:487px;width:660px;height:225px;background:var(--blue);border-radius:8px}
.schedule h2{position:absolute;left:0;top:20px;width:100%;text-align:center;color:#fff;font-size:32px;font-weight:400}
.schedule p{position:absolute;left:0;top:65px;width:100%;text-align:center;color:#fff;font-size:13px}
.field{position:absolute;background:#fff;font-size:12px;color:#777;padding:0 16px;display:flex;align-items:center}
.sched-submit{position:absolute;left:497px;top:103px;width:125px;height:85px;background:#fff;color:var(--blue);font-weight:600;font-size:15px;display:flex;flex-direction:column;align-items:center;justify-content:center;gap:6px}

/* section titles */
.sec-title{left:0;width:1200px;text-align:center;font-size:32px;font-weight:400;line-height:40px}
.sec-title b{font-weight:700}
.rule{height:3px;background:var(--ink)}

/* services */
.svc{width:218px;height:146px;background:#fff;box-shadow:0 4px 18px rgba(0,0,0,.09);border-bottom:4px solid var(--blue);text-align:center}
.svc h3{position:absolute;left:0;top:56px;width:100%;font-size:16px;font-weight:600}
.svc p{position:absolute;left:16px;top:82px;width:186px;font-size:11px;color:var(--muted);line-height:20px}
.svc-icon{width:88px;height:88px;border-radius:50%;background:#d6e6f0;display:flex;align-items:center;justify-content:center}
.svc-icon span{width:64px;height:64px;border-radius:50%;background:var(--blue);display:flex;align-items:center;justify-content:center}

/* about */
.photo{background:linear-gradient(135deg,#cfc9bf,#8d8579)}
.about-title{left:631px;top:1150px;font-size:31px;line-height:41px;font-weight:400}
.about-text{left:631px;top:1265px;width:430px;font-size:12.5px;line-height:22.2px;color:var(--muted)}
.btn-blue{background:var(--blue);color:#fff;font-size:13px;font-weight:600;display:flex;align-items:center;justify-content:center}

/* videos */
.sub{left:270px;top:1706px;width:660px;text-align:center;font-size:12.5px;line-height:22px;color:var(--muted)}
.video{width:312px;height:287px;background:#fff;box-shadow:0 4px 18px rgba(0,0,0,.09)}
.video .thumb{position:absolute;left:0;top:0;width:100%;height:187px;background:linear-gradient(135deg,#b8aa98,#6b6358)}
.video .play{position:absolute;left:133px;top:70px;width:46px;height:46px;border-radius:50%;background:#fff;display:flex;align-items:center;justify-content:center}
.video h4{position:absolute;left:26px;top:198px;font-size:16px;font-weight:600}
.video p{position:absolute;left:26px;top:224px;width:250px;font-size:11px;line-height:20px;color:var(--muted)}

/* help */
.help{left:88px;top:2201px;width:1024px;height:379px;background:var(--dark-box)}
.help-title{left:150px;top:2244px;font-size:42px;line-height:49px;color:#fff;font-weight:400}
.help-title b{font-weight:700}
.help-text{left:150px;top:2376px;width:485px;font-size:12.5px;line-height:22px;color:#fff}
.help-btn{left:150px;top:2478px;width:285px;height:42px}
.worker{left:760px;top:2119px;width:305px;height:461px;background:linear-gradient(180deg,#2f63b5 0%,#1f4a8f 60%,#253a5c 100%);border-radius:120px 120px 0 0}

/* testimonials */
.testi{width:312px;height:252px;background:#fff;box-shadow:0 4px 18px rgba(0,0,0,.09);text-align:center}
.avatar{position:absolute;left:118px;top:16px;width:76px;height:76px;border-radius:50%;background:linear-gradient(180deg,#c9d4df,#8aa2b8)}
.testi h4{position:absolute;left:0;top:100px;width:100%;font-size:18px;font-weight:400}
.testi h4 b{font-weight:600}
.testi p{position:absolute;left:16px;top:128px;width:280px;font-size:12px;font-style:italic;line-height:22px;color:var(--muted)}
.dots{position:absolute;left:110px;top:230px;display:flex;gap:6px}
.dots i{display:block;width:26px;height:2px;background:var(--ink)}
.dots i.on{background:var(--blue)}

/* footer */
.footer{left:0;top:3430px;width:1200px;height:486px;background:var(--dark)}
.form{left:196px;top:3100px;width:806px;height:424px;background:var(--blue)}
.form label{position:absolute;color:#fff;font-size:12px;font-weight:500}
.form .in{position:absolute;background:#fff;font-size:12px;color:#999;padding:0 16px;display:flex;align-items:center}
.form-submit{position:absolute;left:352px;top:350px;width:117px;height:44px;border:2px solid #fff;color:#fff;font-weight:600;font-size:15px;display:flex;align-items:center;justify-content:center}
.f-title{top:3590px;color:#fff;font-size:22px;font-weight:400}
.f-list{color:#ddd;font-size:12.5px;line-height:22px;list-style:none}
.f-list li::before{content:"›";margin-right:8px}
.f-contact{color:#ddd;font-size:12.5px;line-height:18px}
.f-contact div{position:relative;padding-left:24px;margin-bottom:18px}
.f-contact svg{position:absolute;left:0;top:2px}
.f-logo{left:150px;top:3620px;display:flex;flex-direction:column;align-items:center;gap:8px;width:140px}
.f-logo .mark{width:64px;height:64px;border-radius:50%;border:3px solid #fff}
.f-logo .name{color:#fff;font-size:16px;font-weight:700}
.social{top:3741px;width:24px;height:24px;border-radius:50%;border:1px solid #888}
.news{left:818px;top:3699px;width:262px;height:46px;background:#fff;display:flex;align-items:center;padding:0 18px;font-size:12px;color:#555;gap:8px}
.map{left:600px;top:3660px;width:160px;height:120px;background:#353535;border-radius:40px;opacity:.7}
.copy{left:0;top:3878px;width:1200px;text-align:center;color:#ccc;font-size:12px}
.copy-line{left:0;top:3856px;width:1200px;height:1px;background:#3d3d3d}
</style>
</head>
<body>

<!-- header -->
<header class="abs header">
  <div class="abs logo"><div class="logo-mark"></div><div class="logo-name">KP Ductworks</div></div>
  <nav class="abs nav">
    <span style="left:265px">Home</span>
    <span style="left:335px">About us</span>
    <span style="left:423px">Services</span>
    <span style="left:506px">Client testimonials</span>
    <span style="left:656px">Estimate request</span>
    <span style="left:794px">Contact Us</span>
  </nav>
</header>
<div class="abs topbar"></div>
<div class="abs topbar-item" style="left:430px">
  <svg width="12" height="12" viewBox="0 0 24 24" fill="#fff"><path d="M6.6 10.8a15.1 15.1 0 0 0 6.6 6.6l2.2-2.2c.3-.3.7-.4 1-.2 1.1.4 2.3.6 3.6.6.6 0 1 .4 1 1V20c0 .6-.4 1-1 1A17 17 0 0 1 3 4c0-.6.4-1 1-1h3.5c.6 0 1 .4 1 1 0 1.3.2 2.5.6 3.6.1.3 0 .7-.2 1z"/></svg>0123.456.789</div>
<div class="abs topbar-item" style="left:604px">
  <svg width="13" height="11" viewBox="0 0 24 18" fill="#fff"><path d="M0 0h24v2L12 10 0 2z M0 5l12 8 12-8v13H0z"/></svg>email@example.com</div>
<div class="abs topbar-item" style="left:818px"><span class="flag"></span>
  <svg width="10" height="8" viewBox="0 0 10 6"><path d="M1 1l4 4 4-4" stroke="#fff" fill="none" stroke-width="1.5"/></svg></div>
<div class="abs emergency">
  <div class="ring">24/7</div>
  <div class="lbl">Emergency Responce</div>
  <div class="num">0123.456.789</div>
</div>

<!-- hero -->
<section class="abs hero" role="img" aria-label="Plumber working under a kitchen sink"></section>
<h1 class="abs hero-title">Expert <b>Plumbing<br>Contractors</b> You Can<br>Trust</h1>
<p class="abs hero-text">It is a long established fact that a reader will be distracted by the readable content of a page when looking at its layout.</p>
<a class="abs btn-white hero-btn">Learn More</a>

<div class="abs schedule">
  <h2>Schedule A <b>Service</b></h2>
  <p>Feel Out The Form Below</p>
  <div class="field" style="left:36px;top:103px;width:220px;height:37px">Name*</div>
  <div class="field" style="left:266px;top:103px;width:220px;height:37px">Email*</div>
  <div class="field" style="left:36px;top:152px;width:220px;height:36px">Phone*</div>
  <div class="field" style="left:266px;top:152px;width:220px;height:36px">Select Service*</div>
  <div class="sched-submit">
    <svg width="24" height="22" viewBox="0 0 24 22" fill="#0a5b8c"><path d="M0 9L24 0 18 22 11 14 20 4 8 12z"/></svg>Submit</div>
</div>

<!-- services -->
<h2 class="abs sec-title" style="top:794px"><b>Our</b> Services</h2>
<div class="abs rule" style="left:569px;top:838px;width:64px"></div>

<div class="abs svc" style="left:141px;top:908px"><h3>Emergency Plumbing</h3><p>It is a long established fact that a reader will be distracted...</p></div>
<div class="abs svc" style="left:376px;top:908px"><h3>Plumbing and Drains</h3><p>It is a long established fact that a reader will be distracted...</p></div>
<div class="abs svc" style="left:608px;top:908px"><h3>Water Damage</h3><p>It is a long established fact that a reader will be distracted...</p></div>
<div class="abs svc" style="left:843px;top:908px"><h3>Water Heaters</h3><p>It is a long established fact that a reader will be distracted...</p></div>

<div class="abs svc-icon" style="left:206px;top:862px"><span><svg width="32" height="32" viewBox="0 0 32 32" fill="none" stroke="#fff" stroke-width="2"><circle cx="16" cy="17" r="10"/><path d="M16 11v6l4 3M12 4h8"/></svg></span></div>
<div class="abs svc-icon" style="left:440px;top:862px"><span><svg width="32" height="32" viewBox="0 0 32 32" fill="none" stroke="#fff" stroke-width="2"><path d="M10 4v12a6 6 0 0 0 12 0V4M6 4h8M18 4h8M16 22v6"/></svg></span></div>
<div class="abs svc-icon" style="left:673px;top:862px"><span><svg width="32" height="32" viewBox="0 0 32 32" fill="none" stroke="#fff" stroke-width="2"><rect x="5" y="12" width="22" height="12" rx="2"/><path d="M8 18c3-3 5 3 8 0s5 3 8 0M16 4v5"/></svg></span></div>
<div class="abs svc-icon" style="left:908px;top:862px"><span><svg width="32" height="32" viewBox="0 0 32 32" fill="none" stroke="#fff" stroke-width="2"><rect x="9" y="4" width="14" height="24" rx="2"/><circle cx="16" cy="13" r="3"/><path d="M13 22h6"/></svg></span></div>

<!-- about -->
<div class="abs photo" style="left:135px;top:1154px;width:227px;height:206px" role="img" aria-label="Plumber standing with a wrench"></div>
<div class="abs photo" style="left:135px;top:1366px;width:227px;height:135px" role="img" aria-label="Plumber kneeling beside a toolbox"></div>
<div class="abs photo" style="left:368px;top:1154px;width:227px;height:347px" role="img" aria-label="Plumber repairing pipes under a sink"></div>
<h2 class="abs about-title">About Us<br><b>KP Ductworks</b></h2>
<div class="abs rule" style="left:631px;top:1244px;width:62px"></div>
<p class="abs about-text">It is a long established fact that a reader will be distracted by the readable content of a page when looking at its layout. The point of using Lorem Ipsum is that it has a more-or-less normal distribution of letters, as opposed to using 'Content here, content here', making it look like readable English. Many desktop publishing packages and web page editors now use Lorem Ipsum as their default model text, and a search for 'lorem ipsum' will uncover many web sites still in their infancy.</p>
<a class="abs btn-blue" style="left:631px;top:1454px;width:136px;height:43px">Read More</a>

<!-- videos -->
<h2 class="abs sec-title" style="top:1594px">Transform Your <b>Space</b> with Custom<br><b>Windows</b> and Doors</h2>
<p class="abs sub">Watch how we bring your vision to life. From measurement to installation, see the process that ensures a perfect fit every time.</p>

<div class="abs video" style="left:114px;top:1763px">
  <div class="thumb" role="img" aria-label="Plumber showing a client a kitchen cabinet"></div>
  <div class="play"><svg width="16" height="18" viewBox="0 0 16 18"><path d="M2 1l13 8-13 8z" fill="#0a5b8c"/></svg></div>
  <h4>Heading Some Goes Here</h4><p>It is a long established fact that a reader will be distracted...</p>
</div>
<div class="abs video" style="left:443px;top:1763px">
  <div class="thumb" role="img" aria-label="Plumber fixing a drain pipe"></div>
  <div class="play"><svg width="16" height="18" viewBox="0 0 16 18"><path d="M2 1l13 8-13 8z" fill="#0a5b8c"/></svg></div>
  <h4>Heading Some Goes Here</h4><p>It is a long established fact that a reader will be distracted...</p>
</div>
<div class="abs video" style="left:773px;top:1763px">
  <div class="thumb" role="img" aria-label="Plumber sitting with a toolbox in a kitchen"></div>
  <div class="play"><svg width="16" height="18" viewBox="0 0 16 18"><path d="M2 1l13 8-13 8z" fill="#0a5b8c"/></svg></div>
  <h4>Heading Some Goes Here</h4><p>It is a long established fact that a reader will be distracted...</p>
</div>

<!-- help -->
<section class="abs help" role="img" aria-label="Dark workshop background with tools"></section>
<div class="abs worker" role="img" aria-label="Plumber in blue overalls and hard hat holding a hammer"></div>
<h2 class="abs help-title"><b>Need</b> Help<br><b>Contact</b> Us Now!</h2>
<p class="abs help-text">Lorem ipsum dolor sit amet, consectetur adipiscing elit, sed do eiusmod tempor incididunt ut labore et dolore magna aliqua. Quis ipsum suspendisse ultrices gravida. Risus commodo viverra maecenas accumsan lacus vel facilisis.</p>
<a class="abs btn-white help-btn">Request A Free Estimate Today!</a>

<!-- testimonials -->
<h2 class="abs sec-title" style="top:2671px">What Our <b>Client</b> Says</h2>
<div class="abs rule" style="left:569px;top:2723px;width:64px"></div>

<div class="abs testi" style="left:114px;top:2749px"><div class="avatar" role="img" aria-label="Client portrait"></div><h4><b>John</b> Doe</h4><p>It is a long established fact that a reader will be distracted by the readable content of a page when looking at its layout. The point of using Lorem Ipsum.</p><div class="dots"><i></i><i></i><i class="on"></i></div></div>
<div class="abs testi" style="left:443px;top:2749px"><div class="avatar" role="img" aria-label="Client portrait"></div><h4><b>John</b> Doe</h4><p>It is a long established fact that a reader will be distracted by the readable content of a page when looking at its layout. The point of using Lorem Ipsum.</p><div class="dots"><i></i><i></i><i class="on"></i></div></div>
<div class="abs testi" style="left:773px;top:2749px"><div class="avatar" role="img" aria-label="Client portrait"></div><h4><b>John</b> Doe</h4><p>It is a long established fact that a reader will be distracted by the readable content of a page when looking at its layout. The point of using Lorem Ipsum.</p><div class="dots"><i></i><i></i><i class="on"></i></div></div>

<!-- footer -->
<footer class="abs footer"></footer>
<div class="abs form">
  <label style="left:54px;top:38px">First Name</label>
  <div class="in" style="left:55px;top:64px;width:345px;height:41px">First Name</div>
  <label style="left:417px;top:38px">Last Name</label>
  <div class="in" style="left:417px;top:64px;width:347px;height:41px">Last Name</div>
  <label style="left:54px;top:123px">Email</label>
  <div class="in" style="left:55px;top:149px;width:345px;height:41px">Email address</div>
  <label style="left:417px;top:123px">Phone</label>
  <div class="in" style="left:417px;top:149px;width:347px;height:41px">Phone</div>
  <label style="left:53px;top:208px">Message</label>
  <div class="in" style="left:53px;top:233px;width:711px;height:100px;align-items:flex-start;padding-top:12px">Type your questions</div>
  <div class="form-submit">Submit</div>
</div>

<div class="abs f-logo"><div class="mark"></div><div class="name">KP Ductworks</div></div>
<div class="abs social" style="left:155px"></div>
<div class="abs social" style="left:186px"></div>
<div class="abs social" style="left:218px"></div>
<div class="abs social" style="left:250px"></div>

<h3 class="abs f-title" style="left:377px">Quick links</h3>
<ul class="abs f-list" style="left:377px;top:3641px">
  <li>Home</li><li>about us</li><li>services</li><li>client testimonials</li><li>estimate request</li><li>contact us</li>
</ul>

<div class="abs map" role="img" aria-label="Faint world map"></div>
<h3 class="abs f-title" style="left:552px">Contact info</h3>
<div class="abs f-contact" style="left:552px;top:3641px;width:240px">
  <div><svg width="13" height="11" viewBox="0 0 24 18" fill="#ddd"><path d="M0 0h24v2L12 10 0 2z M0 5l12 8 12-8v13H0z"/></svg>Email:<br>email@example.com</div>
  <div><svg width="12" height="12" viewBox="0 0 24 24" fill="#ddd"><path d="M6.6 10.8a15.1 15.1 0 0 0 6.6 6.6l2.2-2.2c.3-.3.7-.4 1-.2 1.1.4 2.3.6 3.6.6.6 0 1 .4 1 1V20c0 .6-.4 1-1 1A17 17 0 0 1 3 4c0-.6.4-1 1-1h3.5c.6 0 1 .4 1 1 0 1.3.2 2.5.6 3.6.1.3 0 .7-.2 1z"/></svg>Phone:<br>0123.456.789</div>
  <div><svg width="11" height="14" viewBox="0 0 20 26" fill="#ddd"><path d="M10 0a10 10 0 0 0-10 10c0 7 10 16 10 16s10-9 10-16A10 10 0 0 0 10 0zm0 14a4 4 0 1 1 0-8 4 4 0 0 1 0 8z"/></svg>Location:<br>Some address line here<br>Example County ZZ9 9ZZ</div>
</div>

<h3 class="abs f-title" style="left:818px">Newsletter</h3>
<p class="abs f-contact" style="left:818px;top:3641px;width:240px">Subscribe to our email address to get the latest news.</p>
<div class="abs news">
  <svg width="13" height="11" viewBox="0 0 24 18" fill="#0a5b8c"><path d="M0 0h24v2L12 10 0 2z M0 5l12 8 12-8v13H0z"/></svg>
  <span style="flex:1">Enter your email...</span>
  <svg width="16" height="15" viewBox="0 0 24 22" fill="#0a5b8c"><path d="M0 9L24 0 18 22 11 14 20 4 8 12z"/></svg>
</div>

<div class="abs copy-line"></div>
<p class="abs copy">© Copyright 2024 | All Right Reserveds</p>

</body>
</html>
```